Business Card Design for ClearPathVitality

We need the new logo on a business card for 3 employees:
Nora Kettering, PhD, Advanced Instructor and Practitioner of SomaLink Integral Medicine (email: nora@clearpathvitality.com)
Ray Holm, Business Manager (email: ray@clearpathvitality.com)
Bea Marlowe, Administrative Assistant (email: bea@helixsense.com)

Target Market(s)

healthcare professionals

Industry/Entity Type

Alternative Medicine

Contact Information for Business Card

Names, titles, emails (names, titles, emails are in project description), phone, address, website, with logo and tagline. See below for address, phone, website: 418 Alder Ln, Bldg 12, Ste 305
Fernhollow, OR 97412
541-555-2746
www.clearpathvitality.com
Tagline: Roots of Balance, Light of Renewal

Font styles to use
Other font styles liked:
• Gabriela

Colors
00a990
86cfc6
6b449b
b7a5cd
85abd2
abd036

Requirements
Must have
• Colors and style that match the logo design - shades such as blue, green, purple
• Compatible or same font as in the logo
Nice to have
• Nice if it goes with the theme of Nora's last business card - uploaded below
Should not have
• colors or style in conflict with the logo

```html
<!DOCTYPE html>
<html lang="en">
<head>
<meta charset="utf-8">
<title>ClearPathVitality Business Card</title>
<link href="https://fonts.googleapis.com/css2?family=Gabriela&display=swap" rel="stylesheet">
<style>
  :root {
    --page-bg: #ececec;
    --card-blue: #0b6bc6;
    --band-green: #12ab57;
    --card-white: #f6f7f8;
    --brand-purple: #4b2b80;
    --brand-green: #3cb043;
    --text-light: #ffffff;
  }
  * { margin: 0; padding: 0; box-sizing: border-box; }
  html, body {
    width: 1200px; height: 800px; overflow: hidden;
    background: var(--page-bg);
    font-family: "Gabriela", Georgia, serif;
  }
  .sheet {
    width: 1200px; height: 800px;
    display: flex; align-items: center; justify-content: center; gap: 40px;
  }
  .card {
    width: 560px; height: 320px;
    position: relative; overflow: hidden;
    box-shadow: 0 6px 18px rgba(0,0,0,0.18);
  }
  /* Back side */
  .card-back { background: var(--card-blue); color: var(--text-light); }
  .tagline-band {
    position: absolute; left: 0; right: 0; top: 132px; height: 38px;
    background: var(--band-green);
    display: flex; align-items: center; justify-content: center;
  }
  .tagline { font-size: 21px; font-weight: normal; letter-spacing: 0.3px; }
  .contact-lines {
    position: absolute; left: 0; right: 0; top: 182px;
    text-align: center; font-size: 13px; line-height: 1.45;
  }
  .divider { padding: 0 6px; }
  /* Front side */
  .card-front { display: flex; }
  .logo-panel {
    width: 47%; background: var(--card-white);
    display: flex; align-items: center; justify-content: center; gap: 10px;
  }
  .logo-mark { width: 54px; height: 54px; flex: none; }
  .brand-name { font-size: 18px; color: var(--brand-purple); }
  .person-panel {
    width: 53%; background: var(--card-blue); color: var(--text-light);
    padding: 94px 0 0 30px;
  }
  .person-name { font-size: 21px; font-weight: normal; margin-bottom: 6px; }
  .person-title { font-size: 13px; line-height: 1.35; margin-bottom: 18px; }
  .person-email { font-size: 13px; }
</style>
</head>
<body>
  <main class="sheet">
    <section class="card card-back" aria-label="Business card back">
      <div class="tagline-band">
        <p class="tagline">Roots of Balance, Light of Renewal</p>
      </div>
      <div class="contact-lines">
        <p>418 Alder Ln, Bldg 12, Ste 305, Fernhollow, OR 97412</p>
        <p>541-555-2746<span class="divider">|</span>www.clearpathvitality.com</p>
      </div>
    </section>

    <section class="card card-front" aria-label="Business card front">
      <div class="logo-panel">
        <svg class="logo-mark" viewBox="0 0 54 54" aria-hidden="true">
          <circle cx="27" cy="27" r="26" fill="var(--brand-green)"/>
        </svg>
        <span class="brand-name">ClearPathVitality</span>
      </div>
      <div class="person-panel">
        <h1 class="person-name">Nora Kettering, PhD</h1>
        <p class="person-title">Advanced Instructor and Practitioner<br>of SomaLink Integral Medicine</p>
        <p class="person-email">nora@clearpathvitality.com</p>
      </div>
    </section>
  </main>
</body>
</html>
```